Truck Wrap Design for Pell Rovey Haulers

We need a moving box truck wrapped with our catch phrase "We lift, We shift, we'll give your day a lift. Ring Pell Rovey!", our phone number "Call now (948) 312-8061, our FB page, instagram page, QR code, website: pellroveyhaulers.example, professional yet eye catching with our logo (uploaded). Truck information document attached as well showing dimensions of the vehicle. We would like some designs with color rather than black and white options.
Updates

Hey guys. We're really liking the efforts but would like to see more color in the designs. Something professional and simple.

Low design entry and low design quality submissions.

Target Market(s)

Families and older people

Industry/Entity Type

Moving

Requirements
Must have
• Contact information and catch phrase
Nice to have
• Professional and eye catching

```html
<!DOCTYPE html>
<html lang="en">
<head>
<meta charset="utf-8">
<title>Pell Rovey Haulers – Truck Wrap Panels</title>
<link rel="stylesheet" href="https://fonts.googleapis.com/css2?family=Jost:wght@400;500&display=swap">
<style>
  :root {
    --navy: #14305a;
    --navy-deep: #0e2343;
    --accent: #f2922c;
    --paper: #ffffff;
    --stage: #eeeeee;
    --trim: #b9bcbf;
  }
  * { margin: 0; padding: 0; box-sizing: border-box; }
  html, body { width: 813px; height: 1200px; overflow: hidden; background: var(--stage); }
  body { font-family: "Jost", sans-serif; color: var(--navy); position: relative; }

  .side-panel {
    position: absolute; left: 30px; width: 753px; height: 250px;
    background: var(--paper); border: 6px solid var(--trim); border-radius: 18px 4px 4px 4px;
    overflow: hidden;
  }
  .side-panel--driver { top: 50px; }
  .side-panel--curb { top: 370px; border-radius: 4px 18px 4px 4px; }

  .hero-art {
    position: absolute; top: 12px; bottom: 0; width: 440px; background: var(--navy);
    clip-path: polygon(0 100%, 0 45%, 45% 0, 100% 55%, 100% 100%);
  }
  .side-panel--driver .hero-art { left: 10px; }
  .side-panel--curb .hero-art { right: 40px; clip-path: polygon(0 100%, 0 55%, 55% 0, 100% 45%, 100% 100%); }

  .accent-band {
    position: absolute; left: 0; right: 0; bottom: 0; height: 8px; background: var(--accent);
  }

  .hero-copy {
    position: absolute; bottom: 30px; color: var(--paper); text-align: center; width: 250px;
  }
  .side-panel--driver .hero-copy { left: 40px; }
  .side-panel--curb .hero-copy { right: 60px; }
  .tagline { font-size: 14px; font-weight: 500; line-height: 1.15; }
  .call { margin-top: 12px; font-size: 11px; font-weight: 500; }
  .call strong { font-size: 17px; font-weight: 500; letter-spacing: .5px; color: var(--accent); }

  .social {
    position: absolute; top: 20px; display: flex; align-items: center; gap: 6px;
    font-size: 13px; font-weight: 500;
  }
  .side-panel--driver .social { left: 20px; }
  .side-panel--curb .social { right: 20px; }
  .dot { width: 14px; height: 14px; border-radius: 50%; background: var(--accent); display: inline-block; }

  .brand-block {
    position: absolute; top: 0; bottom: 0; width: 250px;
    display: flex; flex-direction: column; align-items: center; justify-content: flex-end;
    padding-bottom: 22px; text-align: center;
  }
  .side-panel--driver .brand-block { right: 10px; }
  .side-panel--curb .brand-block { left: 10px; }
  .brand-mark { width: 60px; height: 60px; background: var(--accent); margin-bottom: 18px; }
  .brand-name { font-size: 22px; font-weight: 500; letter-spacing: 1.5px; line-height: 1.05; text-transform: uppercase; }
  .website { margin-top: 8px; font-size: 14px; font-weight: 500; }

  .front-header {
    position: absolute; left: 80px; top: 745px; width: 250px; height: 90px;
    background: var(--navy); color: var(--paper); border: 6px solid var(--trim);
    border-bottom: 8px solid var(--accent);
    display: flex; align-items: center; justify-content: center; text-align: center;
  }
  .front-header .brand-name { font-size: 20px; }

  .rear-doors {
    position: absolute; left: 440px; top: 745px; width: 330px; height: 265px;
    border: 8px solid var(--paper); outline: 2px solid var(--trim);
    display: grid; grid-template-columns: 1fr 1fr; gap: 4px; background: var(--trim);
  }
  .door { background: var(--navy); color: var(--paper); position: relative; text-align: center; }
  .door--left { display: flex; flex-direction: column; align-items: center; justify-content: center; padding-bottom: 30px; }
  .door--left .brand-mark { width: 50px; height: 50px; margin-bottom: 16px; }
  .door--left .brand-name { font-size: 16px; }
  .door--right { padding-top: 26px; font-size: 11px; font-weight: 500; }
  .door--right .social { position: static; justify-content: center; font-size: 11px; margin-bottom: 10px; }
  .door--right .dot { width: 11px; height: 11px; }
  .door--right .tagline { font-size: 11px; padding: 0 8px; }
  .door--right .rear-call { margin-top: 26px; }
  .door--right .rear-call strong { display: block; font-size: 16px; color: var(--accent); }
  .rear-web { position: absolute; left: 0; right: 0; bottom: 22px; font-size: 11px; font-weight: 500; color: var(--paper); text-align: center; }
</style>
</head>
<body>

<section class="side-panel side-panel--driver">
  <div class="social"><span class="dot"></span>@pellrovey</div>
  <div class="hero-art" role="img" aria-label="House outline with hand truck carrying stacked boxes"></div>
  <div class="hero-copy">
    <p class="tagline">We lift, We shift,<br>we'll give your day a lift.</p>
    <p class="call">Call now : <strong>948-312-8061</strong></p>
  </div>
  <div class="brand-block">
    <span class="brand-mark"></span>
    <p class="brand-name">Pell Rovey<br>Haulers</p>
    <p class="website">pellroveyhaulers.example</p>
  </div>
  <div class="accent-band"></div>
</section>

<section class="side-panel side-panel--curb">
  <div class="brand-block">
    <span class="brand-mark"></span>
    <p class="brand-name">Pell Rovey<br>Haulers</p>
    <p class="website">pellroveyhaulers.example</p>
  </div>
  <div class="hero-art" role="img" aria-label="House outline with hand truck carrying stacked boxes"></div>
  <div class="hero-copy">
    <p class="tagline">We lift, We shift,<br>we'll give your day a lift.</p>
    <p class="call">Call now : <strong>948-312-8061</strong></p>
  </div>
  <div class="social"><span class="dot"></span>@pellrovey</div>
  <div class="accent-band"></div>
</section>

<section class="front-header">
  <p class="brand-name">Pell Rovey<br>Haulers</p>
</section>

<section class="rear-doors">
  <div class="door door--left">
    <span class="brand-mark"></span>
    <p class="brand-name">Pell Rovey<br>Haulers</p>
  </div>
  <div class="door door--right">
    <div class="social"><span class="dot"></span>@pellrovey</div>
    <p class="tagline">We lift, We shift,<br>we'll give your day a lift.</p>
    <p class="rear-call">Call now<strong>948-312-8061</strong></p>
  </div>
  <p class="rear-web">pellroveyhaulers.example</p>
</section>

</body>
</html>
```